Restaurant menu design

I need a menu for a restaurant in Spain.
It has to be bohemian but modern. We need something romantic and elegant.
The restaurant is elegant with good food and an excellent reputation. It is also modern at the same time.
The restaurant is superbly decorated and very chick so we need something "class" to fit in with the surroundings.
The size of the document must be 325 mm in high and 245 mm as a maximum and preferably made in indesign.

Reason: Thank you all for your designs.
So far all your designs are ok but it isn´t what we are looking for. Most of the designs are too loaded, too many colors and too much decoration.

Target Market(s)

Adults of various age groups and different nationalities mostly European.

Industry/Entity Type

Restaurant

Requirements
Must have
• The menu must have two interior pages with the text as in the document attached.It must be easily legible.
Nice to have
• See what kind of menus they use in important restaurants in places like Paris, see what designs are in trend, but Not necessarily doing the same style if it doesn’t fit in with the description above.
Should not have
• Nothing old fashioned.

```html
<!DOCTYPE html>
<html lang="es">
<head>
<meta charset="utf-8">
<title>La Galería · Carnes y Postres</title>
<link href="https://fonts.googleapis.com/css2?family=Pinyon+Script&family=Crimson+Text:ital@1&display=swap" rel="stylesheet">
<style>
  :root {
    --ink: #fbf6ee;
    --ink-soft: #efe6d8;
    --title-wine: #7a2a3a;
    --title-red: #c8302c;
    --carnes-top: #a08a6c;
    --carnes-mid: #6b5540;
    --carnes-low: #3a2a20;
    --postres-top: #4a4436;
    --postres-mid: #2f2a22;
    --postres-low: #1e1a15;
  }
  html, body { margin: 0; padding: 0; overflow: hidden; background: #1e1a15; }
  .menu-page {
    position: relative;
    width: 904px;
    height: 1200px;
    overflow: hidden;
    font-family: "Crimson Text", "Times New Roman", serif;
    font-style: italic;
    color: var(--ink);
  }
  .section { position: absolute; left: 0; width: 904px; }
  .section--carnes { top: 0; height: 675px; }
  .section--postres { top: 675px; height: 525px; }
  .section__backdrop { position: absolute; inset: 0; }
  .section--carnes .section__backdrop {
    background:
      radial-gradient(ellipse at 50% 40%, rgba(160,130,95,0.55), transparent 60%),
      linear-gradient(180deg, var(--carnes-top) 0%, var(--carnes-mid) 45%, var(--carnes-low) 100%);
  }
  .section--postres .section__backdrop {
    background:
      radial-gradient(ellipse at 70% 30%, rgba(150,120,80,0.35), transparent 55%),
      linear-gradient(90deg, #3c4530 0%, var(--postres-top) 30%, var(--postres-mid) 70%, var(--postres-low) 100%);
  }
  .section__title {
    position: absolute;
    left: 0; right: 0;
    margin: 0;
    text-align: center;
    font-family: "Pinyon Script", cursive;
    font-style: normal;
    font-weight: 400;
  }
  .section--carnes .section__title { top: 88px; font-size: 40px; color: var(--title-wine); }
  .section--postres .section__title { top: 95px; font-size: 42px; color: var(--title-red); }
  .dish-list {
    position: absolute;
    left: 0; right: 0;
    margin: 0; padding: 0;
    list-style: none;
    text-align: center;
    font-size: 16.5px;
    line-height: 28.65px;
    text-shadow: 0 1px 2px rgba(0,0,0,0.45);
  }
  .section--carnes .dish-list { top: 172px; }
  .section--postres .dish-list { top: 168px; }
  .dish__price { font-size: 13px; margin-left: 1.3em; color: var(--ink-soft); }
  .sauces {
    position: absolute;
    left: 0; right: 0; top: 588px;
    margin: 0;
    text-align: center;
    font-size: 12px;
    text-shadow: 0 1px 2px rgba(0,0,0,0.45);
  }
  .sauces__label {
    font-family: "Pinyon Script", cursive;
    font-style: normal;
    font-size: 19px;
    color: var(--title-red);
  }
  .sauces__price { font-size: 10px; margin-left: 0.8em; }
  .sauces__sep { margin: 0 0.8em; }
  .section-divider {
    position: absolute; left: 0; top: 674px; width: 904px; height: 2px;
    background: #2a231d;
  }
</style>
</head>
<body>
<main class="menu-page">
  <section class="section section--carnes">
    <div class="section__backdrop" role="img" aria-label="Fotografía del comedor del restaurante con arco de piedra, mesas puestas y botellero"></div>
    <h2 class="section__title">Carnes</h2>
    <ul class="dish-list">
      <li>Pechuga de Pollo “Marie France” con Champiñones y Bacon.<span class="dish__price">11,95 €</span></li>
      <li>Chuletas de Cordero.<span class="dish__price">14,50 €</span></li>
      <li>Costillas de Cerdo con Salsa Barbacoa.<span class="dish__price">9,95 €</span></li>
      <li>Paletilla de Cordero Lechal.<span class="dish__price">19,75 €</span></li>
      <li>Le Strogonoff. Finas tiras de Solomillo con su Salsa de Champiñones.<span class="dish__price">15,90 €</span></li>
      <li>Solomillo de Ternera.<span class="dish__price">18,50 €</span></li>
      <li>Solomillo de Ternera a la Ibérica con Jamón Ibérico y Ligera Salsa de Vino Tinto.<span class="dish__price">20,75 €</span></li>
      <li>“Hamburger Castell Steak Haché”. Picada de Solomillo de Ternera, Huevo Frito y Patatas Fritas.<span class="dish__price">14,50 €</span></li>
      <li>Solomillo de Cerdo al Horno con Bacon y su Salsa de Setas.<span class="dish__price">14,25 €</span></li>
      <li>Entrecôte de Ternera.<span class="dish__price">14,75 €</span></li>
      <li>T-Bone Steak de Ternera.<span class="dish__price">16,75 €</span></li>
      <li>Chuletón de Ternera.<span class="dish__price">20,25 €</span></li>
      <li>Parrillada de Carnes y Embutidos.<span class="dish__price">21,50 €</span></li>
    </ul>
    <p class="sauces">
      <span class="sauces__label">Salsas:</span>
      Pimienta.<span class="sauces__price">2,85 €</span><span class="sauces__sep">·</span>
      Roquefort.<span class="sauces__price">2,95 €</span><span class="sauces__sep">·</span>
      Bearnaise.<span class="sauces__price">2,95 €</span><span class="sauces__sep">·</span>
      de Champiñones.<span class="sauces__price">2,65 €</span>
    </p>
  </section>

  <div class="section-divider"></div>

  <section class="section section--postres">
    <div class="section__backdrop" role="img" aria-label="Fotografía del interior del restaurante con plantas de bambú y ventanal al fondo"></div>
    <h2 class="section__title">Los Postres de la Galería</h2>
    <ul class="dish-list">
      <li>Frambuesas “La Galería”.<span class="dish__price">6,25 €</span></li>
      <li>Cocktail de Frutas Exóticas.<span class="dish__price">5,25 €</span></li>
      <li>Sorbete de Limón, Coulis de Fresa y Vodka.<span class="dish__price">5,50 €</span></li>
      <li>Pastel de Chocolate Casero con su Salsa de Vainilla.<span class="dish__price">6,25 €</span></li>
      <li>Crème Brulée.<span class="dish__price">6,25 €</span></li>
      <li>Tarta de Manzana Casera “Tatin” y su Helado de Vainilla.<span class="dish__price">6,95 €</span></li>
      <li>Copa Nevada.<span class="dish__price">6,75 €</span></li>
      <li>Pera al Chocolate Caliente y Helado de Macadamia.<span class="dish__price">5,95 €</span></li>
      <li>Tarta de Queso con Coulis de Fresa.<span class="dish__price">5,75 €</span></li>
      <li>Nuestra Mousse de Chocolate.<span class="dish__price">5,75 €</span></li>
    </ul>
  </section>
</main>
</body>
</html>
```